business card - Helicopter Flight Services, Flight School, etc.

We need a business card design for a new helicopter service.

We offer Helicopter Flight Services, Aerial Filming & Photography, Flight School, and Helicopter Tours. In that order.

Summit Bladecraft, Inc.
Dennis Holbrook
SummitBladecraft@Mailvento.com
818-555-0142

Based at the Brackley Field Airport in Van Nuys, CA. The final design should communicate integrity and safety. Pictures or logos at your discretion.

Card back side - surprise me.

```html
<!DOCTYPE html>
<html lang="en">
<head>
<meta charset="utf-8">
<title>Summit Bladecraft, Inc. — Business Card</title>
<link rel="stylesheet" href="https://fonts.googleapis.com/css2?family=Merriweather:wght@700&family=Open+Sans:wght@400&display=swap">
<style>
  :root {
    --page-bg: #e9e7e3;
    --card-white: #ffffff;
    --brand-blue: #2f93cf;
    --brand-blue-light: #5cb8e6;
    --text-grey: #5a5f63;
    --back-deep: #1665ad;
    --back-mid: #2a97d2;
    --back-glow: #5dc1ea;
    --on-blue: #f2f7fb;
  }
  * { box-sizing: border-box; margin: 0; padding: 0; }
  html, body {
    width: 1200px;
    height: 1062px;
    overflow: hidden;
    background: var(--page-bg);
  }
  .sheet {
    width: 1200px;
    height: 1062px;
    display: flex;
    flex-direction: column;
    align-items: center;
    justify-content: center;
    gap: 62px;
  }
  .card {
    width: 700px;
    height: 400px;
    border-radius: 4px;
    box-shadow: 0 6px 18px rgba(0,0,0,0.18);
    position: relative;
    overflow: hidden;
  }
  .card-front {
    background: var(--card-white);
    padding: 0 70px;
    display: flex;
    flex-direction: column;
    justify-content: center;
  }
  .brand-name {
    font-family: "Merriweather", Georgia, serif;
    font-weight: 700;
    font-size: 46px;
    color: var(--brand-blue);
    display: flex;
    align-items: center;
    gap: 16px;
    letter-spacing: -0.5px;
  }
  .brand-dot {
    width: 16px;
    height: 16px;
    border-radius: 50%;
    background: var(--brand-blue);
    flex: none;
  }
  .contact {
    margin-top: 40px;
    font-family: "Open Sans", Arial, sans-serif;
    color: var(--text-grey);
    font-size: 17px;
    line-height: 1.7;
  }
  .contact-name {
    font-size: 24px;
    color: var(--brand-blue);
    margin-bottom: 4px;
  }
  .contact-role { font-size: 17px; color: var(--text-grey); }
  .contact-row { display: flex; align-items: center; gap: 8px; }
  .contact-row + .contact-row { margin-top: 0; }
  .contact-line { display: flex; gap: 24px; }
  .icon { width: 15px; height: 15px; flex: none; }
  .card-back {
    background: radial-gradient(ellipse at 45% 45%, var(--back-glow) 0%, var(--back-mid) 45%, var(--back-deep) 100%);
    display: flex;
    align-items: center;
    justify-content: center;
  }
  .card-back .brand-name {
    color: var(--on-blue);
    font-size: 50px;
  }
  .card-back .brand-dot { background: var(--on-blue); }
</style>
</head>
<body>
<main class="sheet">
  <section class="card card-front">
    <div class="brand-name"><span class="brand-dot"></span>Summit Bladecraft, Inc.</div>
    <div class="contact">
      <div class="contact-name">Dennis Holbrook <span class="contact-role">• Manager</span></div>
      <div class="contact-line">
        <div class="contact-row">
          <svg class="icon" viewBox="0 0 16 16"><path d="M4 1.5l2.2 3-1.4 1.6c.8 1.9 2.3 3.4 4.2 4.2l1.6-1.4 3 2.2-1.2 2.6C7.600 13.400 2.600 8.400 1.400 2.700z" fill="var(--brand-blue)"/></svg>
          <span>818-555-0142</span>
        </div>
        <div class="contact-row">
          <svg class="icon" viewBox="0 0 16 16" fill="none" stroke="var(--brand-blue)" stroke-width="1.2"><circle cx="8" cy="8" r="6.5"/><ellipse cx="8" cy="8" rx="2.8" ry="6.5"/><path d="M1.5 8h13M2.6 4.6h10.8M2.6 11.4h10.8"/></svg>
          <span>www.Harlowgate.com</span>
        </div>
      </div>
      <div class="contact-row">
        <svg class="icon" viewBox="0 0 16 16"><text x="8" y="13" text-anchor="middle" font-family="Arial, sans-serif" font-size="15" fill="var(--brand-blue)">@</text></svg>
        <span>SummitBladecraft@Mailvento.com</span>
      </div>
    </div>
  </section>
  <section class="card card-back">
    <div class="brand-name"><span class="brand-dot"></span>Summit Bladecraft, Inc.</div>
  </section>
</main>
</body>
</html>
```